Design for Cedar Lark Homes real estate agency

Incorporate logo into new business cards. I need to include the Brindley Vance logo incorporated into Cedar Lark Homes on one side of the card (attached). On the other side I see just the icon with "Maren Quill" (attached) with "Connected by Trust" either included as is or removed from logo and rather put as a tag line on the business card separate from the main logo. Contact information:

Maren Quill
Associate Broker
Cell: 730-418-5093
Email: marenquill@cedarlarkhomes.example
Web: www.cedarlarkhomes.example

Target Market(s)

Buyers, Sellers, Builders and Investors of homes and land

Industry/Entity Type

Real Estate Agent

Contact Information for Business Card

My client base tend to be higher end home buyers, sellers, builders and investors. I have been more and more in land and subdivisions for builders and investors. The card should not be cluttered. Clean and simple - yet with an air of exclusive/high end

Colors

Designer to choose colors to be used in the design.

Requirements
Must have
• Must have the logo on one side that has Brindley Vance logo incorporated. The side that has my contact information does not have to have the Brindley Vance logo incorporated.
• Must include "Connected by Trust" tag line either within logo (as is) or removed from logo and included in another position on the side of the business card with contact information.
Should not have
• Should not have Brindley Vance logo incorporated into Cedar Lark Homes logo on both sides of business card. Would like the Cedar Lark Homes logo that has Brindley Logo only on the back side of card without contact information.

```html
<!DOCTYPE html>
<html lang="en">
<head>
<meta charset="utf-8">
<title>Cedar Lark Homes – Business Cards</title>
<link rel="stylesheet" href="https://fonts.googleapis.com/css2?family=Cabin:wght@400;600&family=Cinzel:wght@600&family=Libre+Baskerville:wght@700&display=swap">
<style>
  :root {
    --stage: #0b0b0b;
    --cream: #f8f6ef;
    --brown-dark: #4a3317;
    --brown: #6e4c24;
    --brown-light: #85602f;
    --gold: #d6b24a;
    --gold-deep: #c9a43c;
    --white: #ffffff;
  }
  * { box-sizing: border-box; margin: 0; padding: 0; }
  html, body { width: 1200px; height: 1000px; overflow: hidden; background: var(--stage); }
  .stage {
    width: 1200px; height: 1000px;
    display: flex; align-items: center; justify-content: center; gap: 48px;
  }
  .card {
    position: relative; width: 540px; height: 308px;
    border-radius: 18px; overflow: hidden;
  }

  /* Logo side */
  .card--logo { background: var(--cream); }
  .logo-lockup {
    position: absolute; left: 62px; top: 96px; width: 420px;
  }
  .logo-lockup__row { display: flex; align-items: center; gap: 14px; }
  .logo-lockup__dot { width: 40px; height: 40px; border-radius: 50%; background: var(--gold); flex: none; }
  .logo-lockup__name {
    font-family: "Libre Baskerville", Georgia, serif; font-weight: 700;
    font-size: 34px; color: var(--brown-dark); letter-spacing: -0.5px; white-space: nowrap;
  }
  .logo-lockup__rule { height: 2px; background: var(--brown-dark); margin: 10px 0 6px 54px; }
  .logo-lockup__foot { display: flex; justify-content: flex-end; align-items: flex-start; gap: 12px; }
  .logo-lockup__agent { text-align: center; }
  .logo-lockup__agent-name {
    font-family: "Cinzel", Georgia, serif; font-weight: 600; font-size: 17px;
    letter-spacing: 3px; color: var(--brown-dark); white-space: nowrap;
  }
  .logo-lockup__tagline {
    font-family: "Cabin", Arial, sans-serif; font-size: 9px; letter-spacing: 3.5px;
    color: var(--brown-dark); margin-top: 2px; white-space: nowrap;
  }
  .partner-badge { width: 58px; height: 34px; background: var(--brown-dark); flex: none; }

  /* Contact side */
  .card--contact {
    background: linear-gradient(150deg, var(--brown-light) 0%, var(--brown) 45%, var(--brown-dark) 100%);
  }
  .contact-band { position: absolute; inset: 0; }
  .name-seal {
    position: absolute; left: 30px; top: 54px; width: 200px; height: 200px;
    border-radius: 50%; background: var(--cream);
    display: flex; flex-direction: column; align-items: center; justify-content: center; gap: 14px;
  }
  .name-seal__dot { width: 36px; height: 36px; border-radius: 50%; background: var(--gold); }
  .name-seal__name {
    font-family: "Cinzel", Georgia, serif; font-weight: 600; font-size: 17px;
    letter-spacing: 2px; color: var(--brown-dark);
    white-space: nowrap; text-align: center;
  }
  .contact {
    position: absolute; left: 270px; top: 70px; color: var(--white);
    font-family: "Cabin", Arial, sans-serif;
  }
  .contact__name { font-weight: 600; font-size: 21px; letter-spacing: 1.5px; white-space: nowrap; }
  .contact__title { font-size: 14px; margin-top: -2px; }
  .contact__tagline { color: var(--gold); font-size: 18px; letter-spacing: 0.5px; margin: 12px 0 14px; white-space: nowrap; }
  .contact__list { list-style: none; display: flex; flex-direction: column; gap: 6px; font-size: 13.5px; }
  .contact__item { display: flex; align-items: center; gap: 8px; white-space: nowrap; }
  .contact__icon { width: 17px; height: 17px; flex: none; }
</style>
</head>
<body>
<main class="stage">

  <section class="card card--logo" aria-label="Card logo side">
    <div class="logo-lockup">
      <div class="logo-lockup__row">
        <span class="logo-lockup__dot"></span>
        <span class="logo-lockup__name">Cedar Lark Homes</span>
      </div>
      <div class="logo-lockup__rule"></div>
      <div class="logo-lockup__foot">
        <div class="logo-lockup__agent">
          <div class="logo-lockup__agent-name">MAREN QUILL</div>
          <div class="logo-lockup__tagline">CONNECTED BY TRUST</div>
        </div>
        <div class="partner-badge" role="img" aria-label="Brindley Vance partner badge"></div>
      </div>
    </div>
  </section>

  <section class="card card--contact" aria-label="Card contact side">
    <svg class="contact-band" viewBox="0 0 540 308" preserveAspectRatio="none" aria-hidden="true">
      <defs>
        <linearGradient id="gold-band" x1="0" y1="0" x2="1" y2="1">
          <stop offset="0" stop-color="#dcba55"/>
          <stop offset="1" stop-color="#c49d35"/>
        </linearGradient>
      </defs>
      <polygon points="0,0 218,0 170,308 0,308" fill="url(#gold-band)"/>
    </svg>

    <div class="name-seal">
      <span class="name-seal__dot"></span>
      <span class="name-seal__name">MAREN QUILL</span>
    </div>

    <div class="contact">
      <div class="contact__name">MAREN QUILL</div>
      <div class="contact__title">Associate Broker</div>
      <div class="contact__tagline">CONNECTED BY TRUST</div>
      <ul class="contact__list">
        <li class="contact__item">
          <svg class="contact__icon" viewBox="0 0 20 20" aria-hidden="true">
            <circle cx="10" cy="10" r="10" fill="#fff"/>
            <rect x="7" y="4.5" width="6" height="11" rx="1.2" fill="#4a3317"/>
            <rect x="8" y="6" width="4" height="6.5" fill="#fff"/>
          </svg>
          730-418-5093
        </li>
        <li class="contact__item">
          <svg class="contact__icon" viewBox="0 0 20 20" aria-hidden="true">
            <circle cx="10" cy="10" r="10" fill="#fff"/>
            <rect x="5" y="6.5" width="10" height="7" fill="#4a3317"/>
            <path d="M5 6.5 L10 10.5 L15 6.5" stroke="#fff" stroke-width="1" fill="none"/>
          </svg>
          marenquill@cedarlarkhomes.example
        </li>
        <li class="contact__item">
          <svg class="contact__icon" viewBox="0 0 20 20" aria-hidden="true">
            <circle cx="10" cy="10" r="10" fill="#fff"/>
            <circle cx="10" cy="10" r="5" fill="none" stroke="#4a3317" stroke-width="1.2"/>
            <ellipse cx="10" cy="10" rx="2.2" ry="5" fill="none" stroke="#4a3317" stroke-width="1"/>
            <line x1="5" y1="10" x2="15" y2="10" stroke="#4a3317" stroke-width="1"/>
          </svg>
          www.cedarlarkhomes.example
        </li>
      </ul>
    </div>
  </section>

</main>
</body>
</html>
```